Creative Businesss Card desgin!

Create a business card for our business Gleam window cleaning!
We are open to creative ideas as long as it maintains a professional image.

Target Market(s)

Small Commercial window cleaning clients including car dealerships, strata manager, cafe

Industry/Entity Type

Window Cleaning

Contact Information for Business Card

Daniel Prescott
General Manager
Gleam Window Cleaning

daniel@gleamservices.com.au
pane-care-southbank.com.au
Ph: 1800 GET GLEAM
Mob: 0437 582 061

Colors
fbed22
0392cd

Requirements
Should not have
• Stock window cleaning/ squeegee graphics

```html
<!DOCTYPE html>
<html lang="en">
<head>
<meta charset="utf-8">
<title>Gleam Window Cleaning – Business Card</title>
<link rel="stylesheet" href="https://fonts.googleapis.com/css2?family=Arimo:wght@700&display=swap">
<style>
  :root {
    --backdrop: #cdd4d4;
    --card-blue: #265d88;
    --brand-yellow: #f5ec33;
    --paper-white: #ffffff;
  }
  html, body {
    margin: 0;
    padding: 0;
    width: 1200px;
    height: 801px;
    overflow: hidden;
    background: var(--backdrop);
  }
  .card {
    position: absolute;
    left: 276px;
    top: 170px;
    width: 753px;
    height: 430px;
    display: block;
  }
  .card-face { fill: var(--card-blue); }
  .accent-stripe { fill: var(--brand-yellow); }
  .corner-panel { fill: var(--paper-white); }
  .brand-name,
  .brand-tagline {
    font-family: "Arimo", Arial, sans-serif;
    font-weight: 700;
    fill: var(--brand-yellow);
  }
  .brand-name { font-size: 100px; }
  .brand-tagline { font-size: 33px; }
</style>
</head>
<body>
  <svg class="card" viewBox="0 0 753 430" xmlns="http://www.w3.org/2000/svg" aria-label="Gleam Window Cleaning business card">
    <rect class="card-face" x="0" y="0" width="753" height="430"/>
    <polygon class="accent-stripe" points="554,305 666,305 542,430 429,430"/>
    <polygon class="corner-panel" points="753,220 753,430 542,430"/>
    <text class="brand-name" x="222" y="220" textLength="308" lengthAdjust="spacingAndGlyphs">GLEAM</text>
    <text class="brand-tagline" x="222" y="263" textLength="310" lengthAdjust="spacingAndGlyphs">WINDOW CLEANING</text>
  </svg>
</body>
</html>
```